Marlowcrest Capital Associates
MCA...
Simple
Glen Barstow
General Partner
Do Not Include
glen@mcafundgroup.example
mcafundgroup.example
This needs to look opulent and eye catching yet classical and classy. It should give the feel that I am highly rich and successful yet not trying too hard. Understated and tasteful.
This side should have the company name "Marlowcrest Capital Associates" and also the abbreviation MCA (in some form, you can be creative with this and it can be subtle as well) as that's an easier name for them to remember and is also used in the email/website info. The whole thing should be designed to make them say "wow" but also to inspire enough trust for them to want to invest their $ with me. Offhand, I like black gold and silver as colors, but that's negotiable. Also there needs to be some space in which I could write on the card if necessary.
This
http://www.printwillow.example/editable_crest_business_card-518204736192847301
i like artistically but it isn't classy or professional enough. Below is what I designed quickly myself, but I think they're too boring AND not classy enough. I'd like the MCA to be somehow less prominent yet still conveyed.
here's the other self made one
here' one other card that I really like the classy look of... though I understand there are some "special" and expensive effects involved in this one.
I don't know if you're allowed to include textures, watermarks, foil etc. typically, but feel free to include them (or at least the possibility of them) in this project. Even if I can't get them put into my "free" business cards with the project I can always order them special after.

```html
<!DOCTYPE html>
<html lang="en">
<head>
<meta charset="utf-8">
<title>Marlowcrest Capital Associates — Business Card Concepts</title>
<link rel="stylesheet" href="https://fonts.googleapis.com/css2?family=Cinzel:wght@400;600&family=Cormorant+Garamond:wght@500;600&display=swap">
<style>
  :root {
    --page-brown: #46362c;
    --page-brown-deep: #3a2c23;
    --card-silver-light: #d3d3d6;
    --card-silver: #b9b9bd;
    --card-silver-dark: #a4a4a9;
    --gold: #d8a92c;
    --gold-light: #f1cc5a;
    --ink-black: #0d0d0d;
    --ink-charcoal: #2a2a2a;
    --text-white: #f2f2f2;
    --text-grey: #4a4a4a;
    --folio: #a88a6c;
  }
  * { box-sizing: border-box; margin: 0; padding: 0; }
  html, body { width: 1200px; height: 737px; overflow: hidden; }
  body {
    background: radial-gradient(ellipse at center, var(--page-brown) 0%, var(--page-brown-deep) 100%);
    font-family: "Cormorant Garamond", Georgia, serif;
    position: relative;
  }
  .card {
    position: absolute;
    width: 504px;
    height: 278px;
    border-radius: 20px;
    overflow: hidden;
    background: linear-gradient(160deg, var(--card-silver-light) 0%, var(--card-silver) 55%, var(--card-silver-dark) 100%);
    box-shadow: 0 2px 6px rgba(0,0,0,.35);
  }
  .card--front-a { left: 43px; top: 53px; }
  .card--front-b { left: 653px; top: 53px; }
  .card--back-band { left: 43px; top: 377px; }
  .card--back-black { left: 653px; top: 377px; background: var(--ink-black); }

  .monogram {
    position: absolute;
    left: 34px;
    top: 20px;
    font-family: "Cinzel", "Times New Roman", serif;
    font-weight: 600;
    font-size: 66px;
    line-height: 1;
    letter-spacing: 2px;
    color: var(--gold);
  }
  .company-name {
    position: absolute;
    left: 36px;
    top: 40px;
    font-family: "Cinzel", "Times New Roman", serif;
    font-weight: 600;
    font-size: 12px;
    letter-spacing: .3px;
    color: #8f8f93;
  }
  .web-line {
    position: absolute;
    right: 26px;
    bottom: 20px;
    font-size: 16px;
    font-weight: 600;
    letter-spacing: .6px;
    color: var(--ink-charcoal);
  }
  .accent { color: var(--gold); }

  .info-band {
    position: absolute;
    left: 0; right: 0; bottom: 0;
    height: 98px;
    background: var(--ink-black);
    border-top: 3px solid var(--gold);
  }
  .card--back-black .info-band {
    height: 104px;
    background: linear-gradient(180deg, var(--card-silver-light), var(--card-silver));
    border-top: 3px solid var(--gold);
  }
  .card--back-black .backdrop {
    position: absolute;
    left: 0; right: 0; top: 0; bottom: 104px;
    background: radial-gradient(ellipse at 55% 60%, #1e1e1e 0%, var(--ink-black) 70%);
  }
  .person-name {
    position: absolute;
    left: 24px;
    top: 18px;
    font-family: "Cinzel", "Times New Roman", serif;
    font-weight: 400;
    font-size: 20px;
    letter-spacing: 1px;
    color: var(--gold);
  }
  .person-title {
    position: absolute;
    left: 25px;
    top: 46px;
    font-family: "Cinzel", "Times New Roman", serif;
    font-size: 9px;
    font-weight: 600;
    letter-spacing: 1px;
    color: var(--text-white);
  }
  .card--back-black .person-title { color: var(--ink-charcoal); }
  .contact {
    position: absolute;
    right: 24px;
    top: 14px;
    text-align: right;
    font-size: 16px;
    font-weight: 600;
    line-height: 24px;
    letter-spacing: .5px;
    color: var(--text-white);
  }
  .card--back-black .contact { color: var(--ink-charcoal); top: 18px; }

  .folio {
    position: absolute;
    top: 702px;
    font-size: 12px;
    color: var(--folio);
    font-family: "Cormorant Garamond", Georgia, serif;
  }
  .folio--left { left: 566px; }
  .folio--right { left: 1165px; }
</style>
</head>
<body>
  <section class="card card--front-a" aria-label="Card front, option A">
    <div class="monogram">MCA</div>
    <div class="company-name">Marlowcrest Capital Associates</div>
    <div class="web-line">www.<span class="accent">mca</span>fundgroup.example</div>
  </section>

  <section class="card card--front-b" aria-label="Card front, option B">
    <div class="monogram">MCA</div>
    <div class="company-name">Marlowcrest Capital Associates</div>
    <div class="web-line">www.<span class="accent">mca</span>fundgroup.example</div>
  </section>

  <section class="card card--back-band" aria-label="Card back with black contact band">
    <div class="info-band">
      <div class="person-name">GLEN BARSTOW</div>
      <div class="person-title">MANAGING PARTNER</div>
      <div class="contact">
        323.555.0148<br>
        glen@mcafundgroup.example<br>
        www.mcafundgroup.example
      </div>
    </div>
  </section>

  <section class="card card--back-black" aria-label="Black card back with silver contact band">
    <div class="backdrop" role="img" aria-label="Faint tonal ornamental pattern on black"></div>
    <div class="info-band">
      <div class="person-name">GLEN BARSTOW</div>
      <div class="person-title">MANAGING PARTNER</div>
      <div class="contact">
        323.555.0148<br>
        glen@<span class="accent">mca</span>fundgroup.example<br>
        www.<span class="accent">mca</span>fundgroup.example
      </div>
    </div>
  </section>

  <div class="folio folio--left">98</div>
  <div class="folio folio--right">99</div>
</body>
</html>
```